Flyer-Design für Motorradbranche
Zielgruppe
Wir sind in der Motorradbranche tätig .
Unser Producktportfoglio erstreckt sich von Motorräder über Motorradbekleidung, bis hinzu Events und spezielle Umbauten.
Unsere Zielgruppe ist sehr breit .
Alter: 16-70 Jahre
Da wir Premium-Produkte verkaufen erwarten unsere Kunden gute Qualität.
Aufgabenstellung
Dieser Flyer sollte etwas frischer gestaltet werden und moderner wirken. Dies ist ein Falzflyer, er wird in 3 gleichgrosse teile gefaltet. Das ganze ist eine Mischung zwischen einem Gutschein und einem Flyer der verteilt wird.
Information die enthalten sein müssen:
- Preis: 370 Euro
- Rabat: 30 Euro
- Datum: 20 April & 17 August 2018
Ansonsten ist alles gleich wie auf dem alten Flyer
Auf unserer Webseite ist der Event wie folgt ausgeschrieben:
https://www.rad-kessler.ch/de/events/feel+the+ride+-+in+piste+de+verlon/582
Format: 301 x 214mm
Das Kessler Tour logo sollte verwendet werden.
Wir sind gespannt was euch so einfällt.

```html
<!DOCTYPE html>
<html lang="de">
<head>
<meta charset="utf-8">
<title>Kessler Tour – Falzflyer Innenseite</title>
<link href="https://fonts.googleapis.com/css2?family=Racing+Sans+One&family=Nunito+Sans:wght@400;800;900&display=swap" rel="stylesheet">
<style>
  :root {
    --backdrop: #9c9c9c;
    --paper: #e6e6e6;
    --paper-light: #efefef;
    --paper-dark: #d2d2d2;
    --track: #cfcfcf;
    --ink: #1e1e1e;
    --ink-soft: #2c2c2c;
    --accent: #d3202a;
    --silhouette: #3a3a3a;
    --ornament: rgba(60,60,60,.10);
    --photo-track: #4e5356;
    --photo-grass: #6f8a45;
    --photo-sand: #a88d63;
  }
  * { box-sizing: border-box; margin: 0; padding: 0; }
  html, body { width: 1200px; height: 907px; overflow: hidden; }
  body {
    background: var(--backdrop);
    font-family: "Nunito Sans", Arial, sans-serif;
    color: var(--ink);
    position: relative;
  }
  .flyer {
    position: absolute;
    left: 30px; top: 40px;
    width: 1140px; height: 827px;
    display: flex;
  }
  .panel {
    position: relative;
    width: 380px; height: 100%;
    background: linear-gradient(160deg, var(--paper-light), var(--paper) 55%, var(--paper-dark));
    overflow: hidden;
  }
  .panel + .panel { border-left: 1px solid #c4c4c4; }
  .tyre-track {
    position: absolute;
    background: linear-gradient(180deg, rgba(200,200,200,0), var(--track) 40%, rgba(200,200,200,0));
    opacity: .55;
  }
  .star-group {
    position: absolute;
    width: 90px; height: 86px;
    background: var(--ornament);
  }
  .panel-title {
    position: absolute;
    top: 76px; left: 0; right: 0;
    text-align: center;
    font-family: "Racing Sans One", Impact, sans-serif;
    font-size: 30px;
    font-style: italic;
    color: var(--ink);
    letter-spacing: .5px;
  }
  .idea-text {
    position: absolute;
    left: 52px; top: 152px; width: 300px;
    font-size: 15.5px; line-height: 19px;
    color: var(--ink-soft);
  }
  .idea-text p + p { margin-top: 19px; }
  .idea-text strong { font-weight: 900; }

  .course { position: absolute; left: 32px; width: 318px; font-size: 15.5px; line-height: 19px; color: var(--ink-soft); }
  .course-name { color: var(--accent); font-weight: 900; display: block; }
  .course-photo { position: absolute; right: 0; width: 254px; }

  .offer-list {
    position: absolute; left: 46px; top: 208px; width: 300px;
    list-style: none;
    font-size: 15.5px; line-height: 22.5px; font-weight: 900;
  }
  .offer-list li { padding-left: 9px; text-indent: -9px; }
  .offer-list .note { font-weight: 400; display: block; text-indent: 0; }
  .price {
    position: absolute; top: 432px; left: 0; right: 0; text-align: center;
    font-family: "Racing Sans One", Impact, sans-serif;
    font-style: italic; font-size: 30px; color: var(--accent);
  }
  .dates {
    position: absolute; top: 474px; left: 0; right: 0; text-align: center;
    font-weight: 900; font-size: 15.5px; line-height: 20px; color: var(--ink);
  }
  .signup {
    position: absolute; top: 514px; left: 0; right: 0; text-align: center;
    font-weight: 900; font-size: 16px; line-height: 20px;
  }
  .discount {
    position: absolute; left: 28px; top: 570px; width: 310px; height: 170px;
  }
  .discount-shape {
    position: absolute; inset: 0;
    background: var(--silhouette);
    border-radius: 85px 60px 80px 80px;
  }
  .discount-label {
    position: absolute; left: 86px; top: 52px;
    font-family: "Racing Sans One", Impact, sans-serif;
    font-style: italic; font-size: 22px; line-height: 27px;
    color: #fff; text-align: center;
  }
</style>
</head>
<body>
<main class="flyer">

  <section class="panel panel-idea">
    <div class="tyre-track" style="left:90px;top:380px;width:300px;height:460px;transform:rotate(28deg)" role="img" aria-label="Reifenspur als Hintergrundmuster"></div>
    <div class="star-group" style="left:20px;top:28px" role="img" aria-label="Sternverzierung"></div>
    <div class="star-group" style="left:22px;top:716px" role="img" aria-label="Sternverzierung"></div>
    <h2 class="panel-title">IDEE</h2>
    <div class="idea-text">
      <p>Zusammen wollen wir das Motorrad entdecken.</p>
      <p>Wir alle haben einmal gelernt unser Motorrad zu bewegen. Um aber die physikalischen Abläufe beim Fahren richtig zu verstehen und diese bewusst zu nutzen, braucht es oft viel Übung, Gespräche und einige Tipps. Der 3-stuffige Kurs <strong>FEEL the RIDE</strong> soll Dir die komplexen Abläufe näher bringen,die zum Lenken eines Motorrades nötig sind.</p>
      <p>Unser Ziel ist es mit möglichst viel Spass gemeinsam zu erlernen, auf was wir beim Fahren achten müssen und wie wir unser Motorrad bewusst steuern.</p>
      <p>Die Technik zu verstehen ist genauso wichtig, wie die richtige Sitzposition oder aber auch der passive Schutz durch die Wahl der richtigen Bekleidung. Unsere erfahrenen Instruktoren stehen Dir während dem ganzen Kurs für Fragen zur Verfügung.</p>
      <p>Die Theorie wird visuell auf Grossleinwand unterstützt und es wird viel gefahren</p>
    </div>
  </section>

  <section class="panel panel-courses">
    <div class="tyre-track" style="left:20px;top:-40px;width:230px;height:900px;transform:rotate(12deg)" role="img" aria-label="Reifenspur als Hintergrundmuster"></div>
    <h2 class="panel-title">KURSE</h2>
    <p class="course" style="top:124px"><span class="course-name">BIKE 1:</span>Gemeinsam gehen wir auf die Reise und erarbeiten uns eine solide Grundlage.</p>
    <div class="course-photo" style="top:204px;height:118px;background:linear-gradient(180deg,var(--photo-grass) 0 10%,var(--photo-track) 10%)" role="img" aria-label="Foto: Motorradfahrer in Schräglage auf der Rennstrecke"></div>
    <p class="course" style="top:328px;left:36px"><span class="course-name">BIKE 2:</span>Die erarbeitete Grundlage wird genutzt, um an wichtigen Details zu arbeiten.</p>
    <div class="course-photo" style="top:410px;height:120px;background:linear-gradient(180deg,var(--photo-sand) 0 10%,var(--photo-track) 10%)" role="img" aria-label="Foto: Motorradfahrer in der Kurve auf der Rennstrecke"></div>
    <p class="course" style="top:548px;left:36px"><span class="course-name">BIKE 3:</span>Wir perfektionieren unseren Fahrstil und setzen das erlernte aus den vorhergehen-den Kursen konsequent um.</p>
    <p class="course" style="top:664px;left:35px"><span class="course-name">BIKE 3R:</span>Die Teilnehmer in dieser Gruppe bringen schon einiges an Erfahrung mit und suchen den Einstieg ins Rennpistenfahren.</p>
  </section>

  <section class="panel panel-offer">
    <div class="tyre-track" style="left:10px;top:-60px;width:260px;height:420px;transform:rotate(-30deg)" role="img" aria-label="Reifenspur als Hintergrundmuster"></div>
    <div class="star-group" style="left:270px;top:28px" role="img" aria-label="Sternverzierung"></div>
    <div class="star-group" style="left:266px;top:716px" role="img" aria-label="Sternverzierung"></div>
    <h2 class="panel-title">ANGEBOT</h2>
    <ul class="offer-list">
      <li>- 4 x 20 Min. Theorie</li>
      <li>- 4 x 20 Min. Fahren mit Instruktor <span class="note">(Gruppe max. 10 Teilnehmer)</span></li>
      <li>- 2 x 20 Min. freies Fahren</li>
      <li>- Frühstückskaffee mit Gipfeli</li>
      <li>- Reichhaltiges Mittagessen (Buffet)</li>
      <li>- Kaffee, kalte Getränke und Früchte den ganzen Tag</li>
      <li>- Fun, Fun, Fun</li>
    </ul>
    <p class="price">370,00 EURO</p>
    <p class="dates">20. April &amp; 17. August 2018</p>
    <p class="signup">Anmeldung unter<br>www.feeltheride.ch</p>
    <div class="discount">
      <div class="discount-shape" role="img" aria-label="Motorrad-Silhouette"></div>
      <p class="discount-label">RABATT<br>30,- EURO</p>
    </div>
  </section>

</main>
</body>
</html>
```